Flyer Design removals

Tern Ridge Removals is a family run professional removal company specializing in all aspects of moving for private and business clients. We provide removals from small local moves to complete relocations and we strive to suit your circumstances and budget. Our aim is to offer efficient and effective removal service for reasonable prices. Our removals services are made straightforward and stress-free with our highly experienced team who handle your belongings with the utmost care and consideration.Our many years spent moving people and businesses provide us with the experience needed to make your move stress and hassle free. We can provide a wide range of packing, removal and storage services. Please fill in our quote request form on www.ternridgeremovals.co.uk as accurately as possible and one of our advisors will contact you with a firm quotation. Would you prefer to speak to us, please call today for the best value removal service you can get.
Industry/Entity Type
Business
Look and feel
Each slider illustrates characteristics of the customer's brand and the style your logo design should communicate.

```html
<!DOCTYPE html>
<html lang="en">
<head>
<meta charset="utf-8">
<title>Tern Ridge Removals – Flyer</title>
<link href="https://fonts.googleapis.com/css2?family=Krona+One&family=Bowlby+One&family=Barlow:wght@400;500&display=swap" rel="stylesheet">
<style>
  :root {
    --navy: #2d2a6b;
    --green: #558f2f;
    --white: #ffffff;
    --ink: #111111;
    --photo-warm: #b9793f;
    --photo-leaf: #4f6b3a;
  }
  * { margin: 0; padding: 0; box-sizing: border-box; }
  html, body { width: 868px; height: 1200px; overflow: hidden; background: var(--navy); }
  .flyer { position: relative; width: 868px; height: 1200px; background: var(--navy); overflow: hidden; color: var(--white); font-family: "Barlow", sans-serif; }
  .backdrop { position: absolute; inset: 0; }
  .brand-title { position: absolute; left: 28px; top: 52px; font-family: "Krona One", sans-serif; font-size: 40px; line-height: 1; white-space: nowrap; letter-spacing: -0.5px; }
  .title-rule { position: absolute; left: 201px; top: 109px; width: 667px; height: 2px; background: var(--white); }
  .contact { position: absolute; left: 312px; top: 120px; display: grid; grid-template-columns: 114px auto; row-gap: 0; font-size: 21px; line-height: 26.5px; }
  .contact dt { font-family: "Bowlby One", sans-serif; font-size: 19px; }
  .contact dd { font-weight: 400; }
  .band-name { position: absolute; left: 12px; top: 292px; font-family: "Krona One", sans-serif; font-size: 23px; color: var(--ink); white-space: nowrap; line-height: 1; }
  .band-cta { position: absolute; left: 12px; top: 320px; font-family: "Krona One", sans-serif; font-size: 10px; color: var(--ink); white-space: nowrap; line-height: 1; }
  .band-cta strong { font-size: 15px; font-weight: 400; margin-left: 4px; }
  .social { position: absolute; top: 291px; width: 42px; height: 42px; border: 1.5px solid var(--white); border-radius: 50%; }
  .photo { position: absolute; left: 34px; width: 182px; height: 182px; border-radius: 50%; border: 3px solid var(--white); }
  .photo--loading { top: 380px; background: radial-gradient(circle at 55% 45%, #c79a62, var(--photo-leaf)); }
  .photo--cabinet { top: 567px; background: radial-gradient(circle at 55% 55%, #d08a45, var(--photo-warm)); }
  .photo--team { top: 754px; background: radial-gradient(circle at 50% 70%, #e7e7e7, var(--photo-leaf) 70%); }
  .statement { position: absolute; left: 227px; font-family: "Bowlby One", sans-serif; white-space: nowrap; text-transform: uppercase; }
  .statement--one { top: 378px; font-size: 27px; line-height: 38.5px; }
  .statement--two { top: 592px; font-size: 25px; line-height: 34px; }
  .statement--three { top: 782px; font-size: 27px; line-height: 38.5px; }
  .rule { position: absolute; height: 2px; background: var(--white); }
  .rule--one { left: 227px; top: 574px; width: 641px; }
  .rule--two { left: 218px; top: 745px; width: 650px; }
  .quote-copy { position: absolute; left: 485px; top: 958px; width: 380px; font-size: 20.5px; line-height: 26.5px; }
  .logo-name { position: absolute; left: 60px; top: 1092px; width: 240px; font-family: "Bowlby One", sans-serif; font-size: 30px; line-height: 34px; color: var(--green); }
</style>
</head>
<body>
<main class="flyer">
  <svg class="backdrop" width="868" height="1200" viewBox="0 0 868 1200" aria-hidden="true">
    <rect x="0" y="257" width="868" height="93" fill="var(--green)"/>
    <path d="M0 268 H550 C620 268 660 300 705 356 H0 Z" fill="var(--white)"/>
    <rect x="0" y="1054" width="868" height="146" fill="var(--white)"/>
    <path d="M868 935 H570 C450 935 412 1000 412 1060 C412 1120 385 1170 340 1200 H868 Z" fill="var(--green)"/>
  </svg>

  <h1 class="brand-title">Tern Ridge Removals</h1>
  <div class="title-rule"></div>

  <dl class="contact">
    <dt>Email</dt><dd>info@ternridgeremovals.co.uk</dd>
    <dt>Phone</dt><dd>07700 900418 OR 0333 014 2277</dd>
    <dt>Address</dt><dd>4 Mill Court Ridge Centre Harwood<br>Hertfordshire AB12 3CD</dd>
  </dl>

  <p class="band-name">TERN RIDGE REMOVALS</p>
  <p class="band-cta">GET IN TOUCH FOR A QUOTE AT<strong>WWW.TERNRIDGEREMOVALS.CO.UK</strong></p>
  <span class="social" style="left:680px"></span>
  <span class="social" style="left:746px"></span>
  <span class="social" style="left:812px"></span>

  <div class="photo photo--loading" role="img" aria-label="Mover in green uniform carrying a box from a removal van"></div>
  <div class="photo photo--cabinet" role="img" aria-label="Mover carrying a wooden cabinet"></div>
  <div class="photo photo--team" role="img" aria-label="Two movers carrying a white cabinet outdoors"></div>

  <p class="statement statement--one">Tern Ridge Removals is a family<br>run professional removal<br>company specializing in all<br>aspects of moving for<br>private and business clients</p>
  <div class="rule rule--one"></div>
  <p class="statement statement--two">We provide removals from<br>small local moves to complete<br>relocations and we strive to suit<br>your circumstances and budget</p>
  <div class="rule rule--two"></div>
  <p class="statement statement--three">Our aim is to offer efficient<br>and effective removal service<br>for reasonable prices</p>

  <p class="quote-copy">Please fill in our quote request form on www.ternridgeremovals.co.uk as accurately as possible and one of our advisors will contact you with a firm quotation.<br>Would you prefer to speak to us, please call today for the best value removal service you can get.</p>

  <p class="logo-name">Tern Ridge Removals</p>
</main>
</body>
</html>
```